Quellmont Haus National Website

We need a website to match our Logo. We will be selling american made vapeing Oils, batteries, Cartomizers, Clearomizers. We have a wharehouse location with couches, TVs streaming clipora, vending machine, and the worlds first flavor mixing bar. We have the lowest priced high grade oils. We will send pictures of the location. Relaxed atmoshpere and no lines for purchase. VIP cards for regulars.

(PLEASE KNOW THAT THE LOGO IS THE UPPER RIGHT LOGO ONLY OF THE FOUR ON THE FILE I ATTACHED)
Updates

Keep in mind we are are only looking for concept and a non coded website

Please know that we are looking for a non coded website

Industry/Entity Type

Purchase

Requirements
Must have
• Online cart, Blog,

```html
<!DOCTYPE html>
<html lang="en">
<head>
<meta charset="utf-8">
<title>Quellmont Haus</title>
<link rel="stylesheet" href="https://fonts.googleapis.com/css2?family=Open+Sans:wght@400;600;700&family=Ubuntu:wght@700&family=Arimo:wght@400;700&display=swap">
<style>
:root{
  --black:#000;
  --panel:#0d0d0d;
  --green:#7cc22e;
  --green-dark:#5f9e1c;
  --white:#fff;
  --text:#e6e6e6;
  --muted:#bdbdbd;
  --rule:#333;
}
*{margin:0;padding:0;box-sizing:border-box}
html,body{width:909px;height:1200px;overflow:hidden;background:var(--black)}
body{position:relative;font-family:'Arimo',Arial,sans-serif;color:var(--text)}
.abs{position:absolute}
.header{left:0;top:0;width:909px;height:104px;background:var(--black)}
.brand{font-family:'Open Sans',sans-serif;font-weight:400;color:var(--green);display:flex;align-items:center;gap:8px;white-space:nowrap}
.brand .mark{width:10px;height:10px;background:var(--green)}
.header .brand{left:97px;top:32px;font-size:35px;letter-spacing:-1px}
.cart{left:748px;top:9px;display:flex;align-items:center;gap:8px;font-size:11px;color:var(--white)}
.cart .sep{width:1px;height:16px;background:#444}
.callout{right:93px;top:37px;font-size:10px;color:var(--green)}
.phone{right:93px;top:50px;font-size:22px;font-weight:700;color:var(--white);letter-spacing:.5px}
.nav{left:0;top:104px;width:909px;height:35px;background:linear-gradient(#8fd13c,#6fb325);border-bottom:3px solid #5a9a1d}
.nav a{position:absolute;top:10px;transform:translateX(-50%);font-family:'Open Sans',sans-serif;font-size:11.5px;color:var(--white);text-decoration:none;white-space:nowrap}
.hero{left:0;top:139px;width:909px;height:334px;background:radial-gradient(ellipse at 25% 50%,#c9c2b4,#7a7266 60%,#4d463e);}
.hero-product{left:430px;top:25px;width:390px;height:280px;background:linear-gradient(135deg,#1c1c1c,#3b3b3b);border-radius:4px}
.hero h1{left:90px;top:68px;font-family:'Ubuntu',sans-serif;font-weight:700;font-size:33px;color:var(--white);text-shadow:0 2px 4px rgba(0,0,0,.5);white-space:nowrap}
.hero h2{left:90px;top:114px;font-family:'Ubuntu',sans-serif;font-weight:700;font-size:38px;color:var(--green);letter-spacing:2px;text-shadow:0 2px 4px rgba(0,0,0,.5);white-space:nowrap}
.buy{left:92px;top:187px;width:198px;height:50px;display:flex;align-items:center}
.buy span{height:46px;width:170px;border-radius:23px;background:linear-gradient(#8acb3b,#4f8d17);font-family:'Ubuntu',sans-serif;font-weight:700;font-size:23px;color:var(--white);padding:10px 0 0 22px;white-space:nowrap}
.buy svg{margin-left:-40px}
.arrow{top:122px;width:32px;height:60px;background:rgba(0,0,0,.85);border-radius:3px;display:flex;align-items:center;justify-content:center}
.tagline{left:0;top:473px;width:909px;height:40px;background:linear-gradient(#f2f2f2,#c9c9c9);text-align:center;font-family:'Open Sans',sans-serif;font-weight:600;font-size:14px;color:#8a8a8a;padding-top:10px;letter-spacing:.3px;white-space:nowrap}
.welcome{left:0;top:513px;width:909px;height:180px;background:radial-gradient(ellipse at 50% 30%,#2a2a2a,#101010 70%);text-align:center}
.welcome h3{margin-top:20px;font-family:'Open Sans',sans-serif;font-weight:600;font-size:24px;color:var(--white);display:flex;justify-content:center;align-items:center;gap:8px}
.welcome h3 .brand{font-size:25px}
.welcome p{width:715px;margin:8px auto 0;font-size:10.3px;line-height:16px;color:var(--text)}
.welcome p+p{margin-top:16px}
.section-title{font-family:'Open Sans',sans-serif;font-weight:600;color:var(--white);font-size:20px;border-top:1px solid var(--rule);border-bottom:1px solid var(--rule);white-space:nowrap}
.blog-title{left:98px;top:730px;width:497px;height:29px;line-height:27px}
.post{left:101px;width:495px;height:135px}
.post .thumb{position:absolute;left:0;top:0;width:129px;height:129px;border:2px solid #444}
.post .meta{position:absolute;left:142px;top:2px;font-family:'Open Sans',sans-serif;font-size:9.5px;color:var(--muted);display:flex;gap:16px;white-space:nowrap}
.post h4{position:absolute;left:141px;top:18px;width:360px;font-family:'Open Sans',sans-serif;font-weight:600;font-size:18.5px;line-height:23px;color:var(--green);letter-spacing:.3px}
.post p{position:absolute;left:142px;top:71px;width:355px;font-size:9.6px;line-height:14.5px;color:var(--text)}
.post .more{position:absolute;left:430px;top:123px;font-size:8px;font-style:italic;font-weight:700;color:var(--green);white-space:nowrap}
.divider{left:614px;top:730px;width:1px;height:362px;background:#262626}
.side-title{left:637px;width:168px;height:30px;line-height:28px;font-size:17.5px;letter-spacing:.3px}
.products{left:641px;top:770px;list-style:none;font-size:10px;color:var(--text)}
.products li{height:20.4px;line-height:14px}
.products li::before{content:"";display:inline-block;width:4px;height:4px;border-radius:50%;background:var(--white);margin-right:7px;vertical-align:2px}
.featured{left:638px;top:965px;width:168px;height:126px;border:2px solid #555;background:linear-gradient(#5a5a5a,#d8d8d8 50%,#8c8c8c)}
.footer{left:0;top:1138px;width:909px;height:62px;background:#0a0a0a;border-top:1px solid #1f1f1f}
.footer nav{position:absolute;left:66px;top:16px;font-size:10px;color:var(--white);white-space:nowrap}
.footer nav a{color:var(--white);text-decoration:none}
.footer nav i{font-style:normal;margin:0 7px}
.footer small{position:absolute;left:65px;top:35px;font-size:9.6px;color:var(--text);white-space:nowrap}
.footer .brand{position:absolute;left:632px;top:15px;font-size:22px}
</style>
</head>
<body>
<header class="abs header">
  <div class="abs brand"><span class="mark"></span>Quellmont Haus</div>
  <div class="abs cart">
    <svg width="18" height="15" viewBox="0 0 18 15"><path d="M1 1h3l2 9h9l2-6H5" fill="none" stroke="#7cc22e" stroke-width="1.8"/><circle cx="7" cy="13" r="1.4" fill="#7cc22e"/><circle cx="14" cy="13" r="1.4" fill="#7cc22e"/></svg>
    <span class="sep"></span><span>2 Items</span>
  </div>
  <div class="abs callout">Call now for a free Case Evalution</div>
  <div class="abs phone">1-555-210-4478</div>
</header>

<nav class="abs nav">
  <a href="#" style="left:124px">HOME</a>
  <a href="#" style="left:224px">ABOUT US</a>
  <a href="#" style="left:339px">SERVICES</a>
  <a href="#" style="left:455px">PRODUCTS</a>
  <a href="#" style="left:557px">FAQ</a>
  <a href="#" style="left:642px">BLOG</a>
  <a href="#" style="left:754px">CONTACT US</a>
</nav>

<section class="abs hero" role="img" aria-label="Blurred photo of a person vaping behind an electronic cigarette starter kit">
  <div class="abs hero-product" role="img" aria-label="Boxed starter kit with charger, batteries and cartridges"></div>
  <h1 class="abs">Premium Electronic</h1>
  <h2 class="abs">E- CIGARETTES</h2>
  <div class="abs buy"><span>BUY NOW</span>
    <svg width="58" height="58" viewBox="0 0 58 58"><circle cx="29" cy="29" r="27" fill="#8fd13c" stroke="#5f9e1c" stroke-width="2"/><path d="M14 19h5l4 16h16l4-11H20" fill="none" stroke="#fff" stroke-width="3"/><circle cx="25" cy="41" r="3" fill="#fff"/><circle cx="37" cy="41" r="3" fill="#fff"/></svg>
  </div>
  <div class="abs arrow" style="left:8px"><svg width="14" height="26"><path d="M12 2L2 13l10 11" fill="none" stroke="#fff" stroke-width="2"/></svg></div>
  <div class="abs arrow" style="left:870px"><svg width="14" height="26"><path d="M2 2l10 11L2 24" fill="none" stroke="#fff" stroke-width="2"/></svg></div>
</section>

<div class="abs tagline">THERE IS NO SMOKE,NO ASH, NO MISSNG OUT.JUST SMOOTH TASTE YOU CAN ANYWHERE</div>

<section class="abs welcome">
  <h3>Welcome to <span class="brand">Quellmont Haus</span></h3>
  <p>Lorem Ipsum is simply dummy text of the printing and typesetting industry. Lorem Ipsum has been the industry's standard dummy text ever since the 1500s, when an unknown printer took into electronic typesetting, remaining essentially &nbsp;a galley of type and scrambled it to make a type specimen book. It has survived not only five centuries, but also the it to make a type specimen book. It has survived not only five centuries.</p>
  <p>Lorem Ipsum is simply dummy text of the printing and typesetting industry. Lorem Ipsum has been the industry's standard dummy text ever since the 1500s, when an unknown printer took into electronic typesetting, remaining essentially &nbsp;a galley of type.</p>
</section>

<h2 class="abs section-title blog-title">Latest Blog</h2>

<article class="abs post" style="top:782px">
  <div class="thumb" role="img" aria-label="Hand holding an electronic cigarette" style="background:linear-gradient(135deg,#5a4a3c,#8a7a68)"></div>
  <div class="meta"><span>&#9786; ADMIN</span><span>&#9635; 22 JUN '13</span><span>&#9873; APPLE, TECHNOLOGY</span></div>
  <h4>E-cigarettes outdo smoking-cessation approaches</h4>
  <p>Lorem ipsum dolor sit amet, consectetur adipiscing elit. Aliquam viverra convallis auctor. Sed accumsan libero quis mi commodo et suscipit enim lacinia. Morbi rutrum vulputate est sed faucibus. Nulla...</p>
  <span class="more">More Details &raquo;</span>
</article>

<article class="abs post" style="top:957px">
  <div class="thumb" role="img" aria-label="Blue vaporizer pen held against a tan background" style="background:linear-gradient(135deg,#e0b060,#c08a3a)"></div>
  <div class="meta"><span>&#9786; ADMIN</span><span>&#9635; 22 JUN '13</span><span>&#9873; APPLE, TECHNOLOGY</span></div>
  <h4>E-cigarettes outdo smoking-cessation approaches</h4>
  <p>Lorem ipsum dolor sit amet, consectetur adipiscing elit. Aliquam viverra convallis auctor. Sed accumsan libero quis mi commodo et suscipit enim lacinia. Morbi rutrum vulputate est sed faucibus. Nulla...</p>
  <span class="more">More Details &raquo;</span>
</article>

<div class="abs divider"></div>

<h2 class="abs section-title side-title" style="top:730px">Our Products</h2>
<ul class="abs products">
  <li>With Nicotine</li><li>Without Nicotine</li><li>Batteries</li><li>USB Charger</li><li>Chargers</li><li>Without Nicotine</li>
</ul>
<h2 class="abs section-title side-title" style="top:928px;border-top:none">Featured Products</h2>
<div class="abs featured" role="img" aria-label="Two electronic cigarettes in an open white gift box"></div>

<footer class="abs footer">
  <nav><a href="#">Home</a><i>|</i><a href="#">About Us</a><i>|</i><a href="#">Services</a><i>|</i><a href="#">Products</a><i>|</i><a href="#">FAQ</a><i>|</i><a href="#">Blog</a><i>|</i><a href="#">Contact Us</a></nav>
  <small>Copyright © 2013 Quellmont Haus. All rights reserved.</small>
  <div class="brand">Quellmont Haus</div>
</footer>
</body>
</html>
```